Career-focused learning application platform

We have a K-12 learning application platform designed for grades 6-12 that needs user interface improvements that provide a positive experience for all users (teachers and students). The learning platform provides career-focused math curriculum and career exploration resources. We would like to improve the user-interface with engaging design elements without taking away from the functionality and performance of the platform.

```html
<!DOCTYPE html>
<html lang="en">
<head>
<meta charset="utf-8">
<title>Career Spotlight – Routewise</title>
<link href="https://fonts.googleapis.com/css2?family=Poppins:wght@400;500;600&display=swap" rel="stylesheet">
<style>
:root{
  --teal:#006f6c;
  --orange:#f2672f;
  --page:#fdf8f5;
  --white:#ffffff;
  --ink:#1d1d1d;
  --muted:#4a4a4a;
  --line:#e4e4e4;
}
*{box-sizing:border-box;margin:0;padding:0}
html,body{width:782px;height:1200px;overflow:hidden}
body{position:relative;background:var(--page);font-family:'Poppins',sans-serif;color:var(--ink)}
.abs{position:absolute}

.topbar{left:0;top:0;width:782px;height:49px;background:var(--white);box-shadow:0 1px 3px rgba(0,0,0,.06)}
.brand{left:12px;top:14px;display:flex;align-items:center;gap:6px;font-size:13px;font-weight:600;color:var(--orange)}
.brand-dot{width:12px;height:12px;border-radius:50%;background:var(--orange)}
.top-icon{top:16px}
.avatar{left:616px;top:6px;width:34px;height:34px;border-radius:50%;background:linear-gradient(#c9d3dc,#8fa0b0)}
.user-email{left:657px;top:16px;font-size:10.5px;font-weight:600}

.sidebar{left:0;top:49px;width:106px;height:1151px;background:var(--teal)}
.nav-item{left:0;width:106px;height:32px;padding-left:17px;line-height:32px;font-size:9.5px;font-weight:500;color:var(--white)}
.nav-item.active{background:var(--orange)}

.section-title{left:127px;font-size:17px;font-weight:500}

.spotlight{left:125px;top:97px;width:642px;height:547px;background:var(--white);border-radius:6px;overflow:hidden;box-shadow:0 1px 4px rgba(0,0,0,.05)}
.spotlight-head{height:42px;background:var(--teal);color:var(--white);font-size:17px;font-weight:500;padding-left:11px;line-height:42px}
.label{left:12px;font-size:14.5px;font-weight:500}
.about{left:12px;top:82px;width:620px;font-size:11.1px;line-height:18px;color:var(--muted)}
.earn{top:155px;font-size:11.7px;color:var(--muted)}
.earn b{display:block;font-size:12.8px;font-weight:600;color:var(--ink);margin-top:3px}
.video{left:15px;top:210px;width:612px;height:287px;border-radius:7px;background:linear-gradient(120deg,#3a302c 0%,#9a5a3a 35%,#b9765a 55%,#8a8683 80%,#4b4644 100%)}
.play{left:273px;top:108px}
.btn{height:25px;border-radius:13px;background:var(--orange);color:var(--white);font-size:9px;font-weight:500;text-align:center;line-height:25px;letter-spacing:.3px}
.learn{left:271px;top:507px;width:101px}

.class-card{top:699px;width:203px;height:187px;background:var(--white);border-radius:6px;box-shadow:0 1px 4px rgba(0,0,0,.05)}
.class-card.current{border:1px solid var(--orange)}
.teacher{left:12px;top:12px;display:flex;align-items:center;gap:5px;font-size:10.6px;font-weight:500;color:var(--teal)}
.current .teacher{color:var(--orange)}
.course{left:12px;top:33px;font-size:10px;font-weight:500;line-height:13.5px}
.folder{left:60px;top:77px;width:76px;height:77px;border-radius:3px;background:linear-gradient(160deg,#f1e3b6 0%,#ecc73a 45%,#e6b81c 100%)}
.go{left:51px;top:170px;width:101px}

.sub{left:127px;top:955px;font-size:11.2px;color:var(--muted)}
.lessons{left:125px;top:982px;width:642px;height:184px;background:var(--white);border-radius:6px;overflow:hidden;box-shadow:0 1px 4px rgba(0,0,0,.05)}
.lessons-head{height:36px;background:var(--teal);color:var(--white);font-size:10.6px;font-weight:500}
.lessons-head span,.row span{position:absolute;line-height:inherit}
.row{position:absolute;left:0;width:642px;font-size:10.6px;color:#333;border-bottom:1px solid var(--line)}
.row:last-child{border-bottom:none}
.c1{left:39px}.c2{left:179px}.c3{left:453px}
.due{color:var(--orange);font-weight:500}
</style>
</head>
<body>
<header class="abs topbar">
  <div class="abs brand"><span class="brand-dot"></span>Routewise</div>
  <svg class="abs top-icon" style="left:550px" width="18" height="18" viewBox="0 0 18 18" fill="none" stroke="#222" stroke-width="1.5"><circle cx="8" cy="8" r="6.5"/><path d="M12.8 12.8 17 17"/></svg>
  <svg class="abs top-icon" style="left:584px" width="18" height="18" viewBox="0 0 18 18" fill="none" stroke="#222" stroke-width="1.3"><path d="M4 13V8a5 5 0 0 1 10 0v5l1.5 1.5h-13z"/><path d="M7.5 16a1.5 1.5 0 0 0 3 0"/><circle cx="13.5" cy="12" r="3" fill="var(--orange)" stroke="none"/></svg>
  <div class="abs avatar" role="img" aria-label="User profile photo"></div>
  <div class="abs user-email">jmarlow@learnpath.org</div>
</header>

<nav class="abs sidebar">
  <div class="abs nav-item" style="top:12px">Home</div>
  <div class="abs nav-item active" style="top:51px">Career Tools ⌄</div>
  <div class="abs nav-item" style="top:91px">Classes</div>
  <div class="abs nav-item" style="top:131px">Assessments</div>
</nav>

<h1 class="abs section-title" style="top:61px">Career Spotlight</h1>

<section class="abs spotlight">
  <div class="spotlight-head">Plumbers, Pipefitters, &amp; Steamfitters</div>
  <h2 class="abs label" style="top:56px">WHAT THEY DO</h2>
  <p class="abs about">Assemble, Install,alter, &amp; repair pipelines or pipe systems that carry water, steam, air, or other liquids or gases. May install heating and cooling equipment &amp; mechanical control systems. includes sprinkler fitters.</p>
  <h2 class="abs label" style="top:129px">EARNINGS</h2>
  <div class="abs earn" style="left:12px">Low End<b>$33,460</b></div>
  <div class="abs earn" style="left:104px">Median<b>$56,330</b></div>
  <div class="abs earn" style="left:196px">High End<b>$98,990</b></div>
  <div class="abs video" role="img" aria-label="Video still of copper pipes mounted along a wall">
    <svg class="abs play" width="70" height="70" viewBox="0 0 70 70"><circle cx="35" cy="35" r="34" fill="rgba(255,255,255,.35)"/><circle cx="35" cy="35" r="27" fill="#fff"/><path d="M31 26l13 9-13 9z" fill="var(--orange)"/></svg>
  </div>
  <div class="abs btn learn">LEARN MORE</div>
</section>

<h2 class="abs section-title" style="top:664px">Classes</h2>

<div class="abs class-card" style="left:124px">
  <div class="abs teacher"><svg width="9" height="10" viewBox="0 0 9 10" fill="currentColor"><circle cx="4.5" cy="2.5" r="2.5"/><path d="M0 10a4.5 4 0 0 1 9 0z"/></svg>Math Teacher</div>
  <div class="abs course">Period 1<br>8th Grade Math/Pre-Algebra</div>
  <div class="abs folder" role="img" aria-label="Class folder illustration"></div>
  <div class="abs btn go">GO TO CLASS</div>
</div>
<div class="abs class-card current" style="left:345px">
  <div class="abs teacher"><svg width="9" height="10" viewBox="0 0 9 10" fill="currentColor"><circle cx="4.5" cy="2.5" r="2.5"/><path d="M0 10a4.5 4 0 0 1 9 0z"/></svg>Math Teacher</div>
  <div class="abs course">Period 6<br>Algebra 1</div>
  <div class="abs folder" role="img" aria-label="Class folder illustration"></div>
  <div class="abs btn go">GO TO CLASS</div>
</div>
<div class="abs class-card" style="left:565px">
  <div class="abs teacher"><svg width="9" height="10" viewBox="0 0 9 10" fill="currentColor"><circle cx="4.5" cy="2.5" r="2.5"/><path d="M0 10a4.5 4 0 0 1 9 0z"/></svg>Math Teacher</div>
  <div class="abs course">Period 5<br>Algebra 1</div>
  <div class="abs folder" role="img" aria-label="Class folder illustration"></div>
  <div class="abs btn go">GO TO CLASS</div>
</div>

<h2 class="abs section-title" style="top:927px">Upcoming lessons</h2>
<p class="abs sub">Lessons due up to the next 7 days:</p>

<section class="abs lessons">
  <div class="lessons-head" style="position:relative;line-height:36px"><span class="c1">Class</span><span class="c2">Lesson</span><span class="c3">Due</span></div>
  <div class="row" style="top:36px;height:39px;line-height:39px"><span class="c1">Period 1</span><span class="c2">1.1- Translations</span><span class="c3 due">October 15th at 11:59PM</span></div>
  <div class="row" style="top:75px;height:37px;line-height:37px"><span class="c1">Period 1</span><span class="c2">2.1 - Operations With Rational Numbers</span><span class="c3 due">October 15th at 11:59PM</span></div>
  <div class="row" style="top:112px;height:35px;line-height:35px"><span class="c1">Period 1</span><span class="c2">3.1 - Parallel Lines and Transversals</span><span class="c3 due">October 15th at 11:59PM</span></div>
  <div class="row" style="top:147px;height:37px;line-height:37px;border-bottom:none"><span class="c1">Period 1</span><span class="c2">3.3 - Angle Relationships in Triangles</span><span class="c3 due">October 15th at 11:59PM</span></div>
</section>
</body>
</html>
```